"How it works" illustration

We are a startup that will sell greeting cards to consumers online. Our value proposition is based on convenient delivery of the cards when customer need them. We need an illustration that shows how things will work for our consumers. This illustration will be the most important element on the landing page of our website. The illustrations should be cartoons or drawings that explain simply what customers need to do on each step required to complete a purchase with us. Attached we have a description of each of the steps. Please prepare two versions, one including only the drawings/cartoons (no text) and another one that includes the attached text. The service is targeted for professional women aged between 25 and 40. The design should communicate simplicity and friendlyness. Some of the colors we have in our logo are white, light blue and light grey (you can see our logo on the second slide of the attached file). As a reference we really like the illustrations used by Quillnest on their landing page.

Industry/Entity Type

Delivery

```html
<!DOCTYPE html>
<html lang="en">
<head>
<meta charset="UTF-8">
<title>How it works</title>
<link rel="stylesheet" href="https://fonts.googleapis.com/css2?family=Source+Sans+3:ital,wght@0,400;0,600;0,700;1,400&display=swap">
<style>
  :root {
    --accent: #3fb5e5;
    --ink: #1f1f1f;
    --muted: #9a9a9a;
    --paper: #ffffff;
    --art-light: #eef7fc;
    --art-mid: #cfeaf7;
    --art-grey: #e6e8ea;
  }
  html, body {
    margin: 0;
    padding: 0;
    width: 1200px;
    height: 900px;
    overflow: hidden;
    background: var(--paper);
    font-family: "Source Sans 3", "Myriad Pro", Arial, sans-serif;
  }
  .how-it-works {
    position: relative;
    width: 1200px;
    height: 900px;
  }
  .step-art {
    position: absolute;
    border-radius: 14px;
  }
  .step-art--signup {
    left: 59px; top: 111px; width: 270px; height: 252px;
    background: linear-gradient(160deg, var(--art-mid) 0%, var(--art-grey) 70%, var(--art-light) 100%);
  }
  .step-art--confirm {
    left: 424px; top: 97px; width: 303px; height: 255px;
    background: linear-gradient(160deg, var(--art-grey) 0%, var(--art-mid) 45%, var(--art-light) 100%);
  }
  .step-art--deliver {
    left: 850px; top: 53px; width: 293px; height: 322px;
    background: radial-gradient(circle at 62% 58%, var(--art-mid) 0%, var(--art-light) 55%, var(--art-grey) 100%);
  }
  .step-number {
    position: absolute;
    width: 66px;
    height: 66px;
    border-radius: 50%;
    background: var(--accent);
    color: var(--paper);
    font-size: 40px;
    font-weight: 300;
    line-height: 66px;
    text-align: center;
    top: 389px;
  }
  .step-number--1 { left: 172px; }
  .step-number--2 { left: 566px; }
  .step-number--3 { left: 957px; }
  .step-copy {
    position: absolute;
    top: 480px;
    width: 290px;
  }
  .step-copy--signup { left: 50px; }
  .step-copy--confirm { left: 445px; }
  .step-copy--deliver { left: 836px; }
  .step-title {
    margin: 0 0 6px;
    color: var(--accent);
    font-size: 26px;
    font-weight: 700;
    letter-spacing: 0.2px;
  }
  .step-lead {
    margin: 0 0 10px;
    color: var(--ink);
    font-size: 19.5px;
    line-height: 25.5px;
  }
  .step-aside {
    margin: 0;
    color: var(--muted);
    font-size: 19.5px;
    font-style: italic;
    line-height: 25.5px;
  }
</style>
</head>
<body>
<main class="how-it-works">
  <div class="step-art step-art--signup" role="img" aria-label="Line drawing of a woman at a desktop computer filling in a sign-up form"></div>
  <div class="step-art step-art--confirm" role="img" aria-label="Computer screen showing an email from a winged elephant mascot with a speech bubble reading a birthday reminder"></div>
  <div class="step-art step-art--deliver" role="img" aria-label="Woman waving as the winged elephant mascot flies over a sketched globe among clouds, carrying envelopes"></div>

  <div class="step-number step-number--1">1</div>
  <div class="step-number step-number--2">2</div>
  <div class="step-number step-number--3">3</div>

  <section class="step-copy step-copy--signup">
    <h2 class="step-title">SIGN UP</h2>
    <p class="step-lead">Select all the dates when you’ll need a greeting card</p>
    <p class="step-aside">After that you are done and can relax (maybe go to the beach on vacation)</p>
  </section>

  <section class="step-copy step-copy--confirm">
    <h2 class="step-title">CONFIRM</h2>
    <p class="step-lead">2 weeks before every date we’ll email you to confirm your card selection</p>
    <p class="step-aside">Don’t worry, we won’t harass you with emails… We promise</p>
  </section>

  <section class="step-copy step-copy--deliver">
    <h2 class="step-title">DELIVER</h2>
    <p class="step-lead">We can either send the card directly to the recipient or to you with a “ready to re-send envelope” (postage and everything!)</p>
    <p class="step-aside">Simple, right? Now enjoy the feeling of being an incredibly thoughtful and smart individual</p>
  </section>
</main>
</body>
</html>
```